Business Card Design

We need a business card design for a consulting firm which provides safety and risk management consulting services for public venues, hotels and tourist attractions. The business card design should include the attached logo unedited with a design based on incorporating the existing logo with a design of geometric patterns or lines on a predominantly white background.

Industry/Entity Type

Business

Contact Information for Business Card

Dane Morravik
Director & Principal Consultant

Ph: +61 (0) 478506 214
PO Box 456 Brenmoor Vale, NSW Australia 2611
info@corvalrisksafety.example

(back of card to include website www.corvalrisksafety.example

```html
<!DOCTYPE html>
<html lang="en">
<head>
<meta charset="utf-8">
<title>Corval Risk &amp; Safety – Business Card</title>
<link rel="stylesheet" href="https://fonts.googleapis.com/css2?family=Quicksand:wght@500;600;700&family=Fredoka:wght@600&display=swap">
<style>
  :root {
    --bg: #e4e5e6;
    --card: #ffffff;
    --blue: #1f8fc9;
    --blue-deep: #1565a8;
    --green: #6cbf3f;
    --green-soft: #8fd07a;
    --ink: #3a3a3a;
  }
  * { margin: 0; padding: 0; box-sizing: border-box; }
  html, body { width: 1200px; height: 1200px; overflow: hidden; background: var(--bg); }
  .canvas { position: relative; width: 1200px; height: 1200px; }
  .card {
    position: absolute; left: 180px; width: 840px; height: 480px;
    background: var(--card); overflow: hidden;
    box-shadow: 0 6px 18px rgba(0,0,0,.18);
  }
  .card--brand { top: 80px; }
  .card--contact { top: 640px; }
  .card svg.pattern { position: absolute; inset: 0; width: 100%; height: 100%; }

  .brand-name {
    position: absolute; font-family: "Quicksand", sans-serif; font-weight: 700;
    color: var(--blue); display: flex; align-items: center; white-space: nowrap;
  }
  .brand-name .mark { display: inline-block; background: var(--green); border-radius: 50%; }
  .card--brand .brand-name { left: 210px; top: 262px; font-size: 54px; gap: 20px; }
  .card--brand .brand-name .mark { width: 44px; height: 44px; }
  .card--contact .brand-name { left: 262px; top: 40px; font-size: 32px; gap: 12px; }
  .card--contact .brand-name .mark { width: 26px; height: 26px; }

  .person { position: absolute; left: 262px; top: 104px; }
  .person-name { font-family: "Fredoka", sans-serif; font-weight: 600; font-size: 46px; color: var(--blue); line-height: 1; }
  .person-name .surname { color: var(--green); }
  .person-title { font-family: "Quicksand", sans-serif; font-weight: 600; font-size: 17px; color: var(--ink); margin-top: 6px; }

  .contact-list { position: absolute; left: 180px; top: 206px; list-style: none; font-family: "Quicksand", sans-serif; font-weight: 600; color: var(--ink); }
  .contact-item { display: flex; align-items: center; gap: 16px; margin-bottom: 18px; font-size: 22px; line-height: 1.25; }
  .contact-item svg { flex: none; width: 70px; height: 42px; }
  .contact-item.email { font-size: 21px; }

  .website { position: absolute; right: 64px; bottom: 42px; font-family: "Quicksand", sans-serif; font-weight: 700; font-size: 26px; color: var(--green); }
  .website .domain { color: var(--blue); }
</style>
</head>
<body>
<main class="canvas">

  <section class="card card--brand">
    <svg class="pattern" viewBox="0 0 840 480" role="img" aria-label="Geometric triangle pattern in greens and blues">
      <defs>
        <linearGradient id="tri-a" x1="0" y1="0" x2="1" y2="1">
          <stop offset="0" stop-color="#2a8fcf"/>
          <stop offset=".45" stop-color="#78c96a"/>
          <stop offset=".75" stop-color="#1f7fc0"/>
          <stop offset="1" stop-color="#8fd07a"/>
        </linearGradient>
      </defs>
      <polygon fill="url(#tri-a)" points="0,0 840,0 840,160 800,175 760,240 690,205 610,190 520,150 420,120 330,150 250,110 150,120 90,150 60,210 0,230"/>
      <polygon fill="url(#tri-a)" points="0,380 55,440 30,480 0,480"/>
    </svg>
    <div class="brand-name"><span class="mark"></span>Corval Risk &amp; Safety</div>
  </section>

  <section class="card card--contact">
    <svg class="pattern" viewBox="0 0 840 480" role="img" aria-label="Geometric triangle pattern strips in greens and blues">
      <defs>
        <linearGradient id="tri-b" x1="0" y1="0" x2="0.6" y2="1">
          <stop offset="0" stop-color="#6cbf3f"/>
          <stop offset=".35" stop-color="#1f7fc0"/>
          <stop offset=".65" stop-color="#8fd07a"/>
          <stop offset="1" stop-color="#1565a8"/>
        </linearGradient>
      </defs>
      <polygon fill="url(#tri-b)" points="0,0 225,0 225,70 190,110 225,150 225,480 0,480"/>
      <rect fill="url(#tri-b)" x="812" y="0" width="28" height="480"/>
    </svg>

    <div class="brand-name"><span class="mark"></span>Corval Risk &amp; Safety</div>

    <div class="person">
      <h1 class="person-name">Dane <span class="surname">Morravik</span></h1>
      <p class="person-title">Director &amp; Principal Consultant</p>
    </div>

    <ul class="contact-list">
      <li class="contact-item phone">
        <svg viewBox="0 0 70 42" aria-hidden="true">
          <polygon points="0,0 70,21 0,42" fill="var(--blue)"/>
          <path d="M12 12c2-2 4 2 5 4s-2 3-1 5 3 4 5 5 3-2 5-1 4 3 2 5c-6 5-20-9-16-18z" fill="#fff"/>
        </svg>
        <span>+61 (0) 478506 214</span>
      </li>
      <li class="contact-item address">
        <svg viewBox="0 0 70 42" aria-hidden="true">
          <polygon points="0,0 70,21 0,42" fill="var(--green)"/>
          <path d="M18 8a8 8 0 0 1 8 8c0 6-8 15-8 15s-8-9-8-15a8 8 0 0 1 8-8z" fill="#fff"/>
          <circle cx="18" cy="16" r="3" fill="var(--green)"/>
        </svg>
        <span>PO Box 456 Brenmoor Vale,<br>NSW Australia 2611</span>
      </li>
      <li class="contact-item email">
        <svg viewBox="0 0 70 42" aria-hidden="true">
          <polygon points="0,0 70,21 0,42" fill="var(--blue-deep)"/>
          <rect x="8" y="13" width="22" height="15" fill="#fff"/>
          <path d="M8 13l11 8 11-8" stroke="var(--blue-deep)" stroke-width="2" fill="none"/>
        </svg>
        <span>info@corvalrisksafety.example</span>
      </li>
    </ul>

    <p class="website">www.<span class="domain">corvalrisksafety</span>.example</p>
  </section>

</main>
</body>
</html>
```